Private Lending Company looking to have 3 Word Documents re-formatted, cleaned up and generally made

We have three word documents that we use for presentations.
a) The first document (Wholesale and Portfolio Investor Pack May 2016) has graphs incorporated which are currently blurred and perhaps not the most current data. All graphs have the source noted so these would need to be replaced with current data if it is available and generally cleaned up. The cover page requires our new logo (attached). The illustration on page 29 needs to be changed to a matrix or cube or something that represents/brings all the elements of page 29 (ie 4 bullet points) together. The whole document needs to look more corporate and professional.
b) The second and third documents (Talvora KRB Lending Guides July 2016 and Talvora Select Lending Guides July 2016) both require tidying up. Tables are not quite aligned, data within the tables is not lined up or consistent. Again, both documents need to be polished and given to look more corporate. Ensure the logo in the letterhead is the same size on each page.
Throughout all documents it is important to keep tables, shading, size etc consistent. Any table fill should be in the same blue (as per advert) throughout Documents 2 & 3.
We would like our corporate colours to be used not only in the letterhead but also in the font, the fill in the tables etc.
We have attached our logo, and a digital copy of an advert we recently used. The advert is attached more for your information - you do not need to use it at all.
The colours used in the advert are as follows:
Blue - RGB: R=30, G=30, B=59
Gold - RGB: R=227, G=205, B=152 (for table outlines)
Blue - CMYK: C=97%, M=87%, Y=45%, K=55%
Gold - CMYK: C=12%, M=21%, Y=51%, K=2% (for table outlines)
The blue in our logo is on the standard Word Pallette (Dark Blue, Text 2, Darker 25%)
The light blue featured in the tables of Document 1 can be: Blue, Accent 1, Lighter 80%. This also needs to be used consistently thoughout this document.
We would like all text to be in the same colour as the logo, although of course not necessarily the same font. Our preferred Font is Century Gothic.
Please direct any questions back to us.
It Company
- Calibri

```html
<!DOCTYPE html>
<html lang="en">
<head>
<meta charset="utf-8">
<title>The Opportunity – Portfolio &amp; Asset Management</title>
<link rel="stylesheet" href="https://fonts.googleapis.com/css2?family=Questrial&display=swap">
<style>
  :root {
    --page: #ffffff;
    --ink: #111111;
    --title-ink: #1f3552;
    --rule: #8a8a8a;
    --tile-top: #2c5a8f;
    --tile-bottom: #1a3a66;
    --tile-edge: #6f7f95;
    --frame: #e9ecf2;
    --frame-edge: #9aa1b2;
    --gold: #e3cd98;
    --tile-text: #ffffff;
    --footer-ink: #5a6a80;
  }
  * { margin: 0; padding: 0; box-sizing: border-box; }
  html, body { width: 922px; height: 1200px; overflow: hidden; background: var(--page); }
  body { font-family: "Questrial", "Century Gothic", sans-serif; color: var(--ink); position: relative; }

  .page-title {
    position: absolute; left: 148px; width: 631px; top: 121px; height: 74px;
    border-top: 1px solid var(--rule); border-bottom: 1px solid var(--rule);
    text-align: center; color: var(--title-ink);
    font-size: 30px; font-weight: 700; line-height: 35px; padding-top: 2px;
  }

  .matrix { position: absolute; left: 0; top: 0; width: 922px; height: 640px; }
  .matrix text {
    font-family: "Questrial", "Century Gothic", sans-serif;
    font-size: 23px; font-weight: 700; font-style: italic; fill: var(--tile-text);
  }

  .intro, .capability-heading, .capability-text {
    position: absolute; font-size: 17px; line-height: 22px; font-weight: 400;
  }
  .intro { left: 155px; top: 668px; }
  .capability-heading { left: 155px; font-weight: 700; font-style: italic; }
  .capability-text { left: 210px; width: 540px; }

  .page-footer {
    position: absolute; left: 155px; width: 600px; top: 1160px; height: 20px;
    border-bottom: 1px solid var(--rule);
  }
  .page-number {
    position: absolute; right: -24px; bottom: 2px; font-size: 15px; color: var(--footer-ink);
  }
  .footer-note {
    position: absolute; left: 155px; width: 600px; top: 1182px;
    text-align: center; font-size: 12px; line-height: 14px; color: var(--footer-ink);
  }
</style>
</head>
<body>
  <h1 class="page-title">The Opportunity – Portfolio &amp; Asset<br>Management</h1>

  <svg class="matrix" viewBox="0 0 922 640" role="img" aria-label="Capability matrix joining four services around one centre">
    <defs>
      <linearGradient id="tileFill" x1="0" y1="0" x2="0" y2="1">
        <stop offset="0" stop-color="var(--tile-top)"/>
        <stop offset="1" stop-color="var(--tile-bottom)"/>
      </linearGradient>
    </defs>
    <rect class="matrix-frame" x="216" y="236" width="508" height="368" rx="30"
          fill="var(--frame)" stroke="var(--frame-edge)" stroke-width="1.5"/>
    <g class="matrix-axes" stroke="var(--gold)" stroke-width="4">
      <line x1="470" y1="240" x2="470" y2="600"/>
      <line x1="220" y1="420" x2="720" y2="420"/>
    </g>
    <g class="tiles" fill="url(#tileFill)" stroke="var(--tile-edge)" stroke-width="2.5">
      <rect x="232" y="252" width="226" height="158" rx="20"/>
      <rect x="482" y="252" width="226" height="158" rx="20"/>
      <rect x="232" y="430" width="226" height="158" rx="20"/>
      <rect x="482" y="430" width="226" height="158" rx="20"/>
    </g>
    <circle class="matrix-hub" cx="470" cy="420" r="26" fill="var(--gold)" stroke="var(--page)" stroke-width="5"/>
    <g text-anchor="middle">
      <text x="345" y="326">Origination &amp;</text>
      <text x="345" y="354">assessment</text>
      <text x="595" y="308">Loan</text>
      <text x="595" y="335">documentation</text>
      <text x="595" y="362">&amp; settlement</text>
      <text x="345" y="503">Asset</text>
      <text x="345" y="531">management</text>
      <text x="595" y="503">Portfolio</text>
      <text x="595" y="531">management</text>
    </g>
  </svg>

  <p class="intro">Talvora has ‘end to end’ capabilities.</p>

  <h2 class="capability-heading" style="top:712px">1. Origination &amp; assessment</h2>
  <p class="capability-text" style="top:755px">Build a high yielding portfolio for you from a referral source of over 1200 broker groups nationally.</p>

  <h2 class="capability-heading" style="top:822px">2. Loan documentation &amp; settlement</h2>
  <p class="capability-text" style="top:864px">The experience from our network of professionals for documentation and settlement process.</p>

  <h2 class="capability-heading" style="top:931px">3. Portfolio management</h2>
  <p class="capability-text" style="top:973px">Leverage our portfolio management experience to optimise the management of the portfolio from settlement to discharge.</p>

  <h2 class="capability-heading" style="top:1040px">4. Asset management</h2>
  <p class="capability-text" style="top:1082px">Our proven asset management capabilities to manage assets, instruct third parties and negotiate with borrowers on your behalf.</p>

  <footer>
    <div class="page-footer"><span class="page-number">29</span></div>
    <p class="footer-note">Talvora Securities – Tailored Finance Solutions</p>
  </footer>
</body>
</html>
```